Web design for trailer business

We are a digital marketing company and are rebuilding a website for an established trailer business. Their current website is: https://www.dunlacktrailers.com.au/
They want a new website designed with a similar style to a competitor: https://www.grevikstrailers.com.au/
The three main page styles that need to be done are:
Home page: https://www.grevikstrailers.com.au/
Category page: https://www.grevikstrailers.com.au/machinery-trailers/
Product view page: https://www.grevikstrailers.com.au/8-x-5-tandem-plant-trailer/
Their colour scheme is actually changing to orange and blue instead of yellow and blue. The colours are the ones in the 'Certified By' section of the footer, with the image of VEP International.
Number of Pages Required
3 page
Look and feel
Each slider illustrates characteristics of the customer's brand and the style your logo design should communicate.

```html
<!DOCTYPE html>
<html lang="en">
<head>
<meta charset="utf-8">
<title>Dunlack Trailers</title>
<link rel="stylesheet" href="https://fonts.googleapis.com/css2?family=Roboto+Condensed:wght@400;700&family=Open+Sans:ital,wght@0,400;0,600;0,700;1,400&display=swap">
<style>
:root{
  --orange:#f39a1e;
  --blue:#2f5bb3;
  --blue-deep:#1f3f8f;
  --dark:#141414;
  --ink:#2b2b2b;
  --muted:#666;
  --grey-bg:#ededed;
  --white:#fff;
}
*{box-sizing:border-box;margin:0;padding:0}
html,body{width:1200px;height:5085px;overflow:hidden}
body{font-family:"Open Sans",Arial,sans-serif;color:var(--ink);background:var(--white);position:relative}
.abs{position:absolute}
h1,h2,h3{font-family:"Roboto Condensed","Arial Narrow",sans-serif;font-weight:400}
.btn{display:inline-block;font-size:14px;color:var(--white);text-align:center}
.btn-orange{background:var(--orange);border-radius:3px}
.btn-blue{background:var(--blue);border-radius:3px}

/* hero */
.hero{left:0;top:0;width:1200px;height:680px;background:linear-gradient(160deg,#3d4146 0%,#6d7176 35%,#9a9da0 55%,#4a4d51 100%)}
.topbar{left:0;top:0;width:1200px;height:40px;font-size:12px;color:var(--white)}
.topbar .contact{left:100px;top:12px}
.topbar .contact span{margin-right:24px}
.topbar .right{left:890px;top:10px;display:flex;gap:8px;align-items:center}
.sq{width:16px;height:16px;background:var(--white);border-radius:2px;display:inline-block}
.brand{left:90px;top:62px;display:flex;align-items:center;gap:12px;color:var(--white);font-family:"Open Sans",sans-serif;font-weight:600;font-size:20px}
.brand i{width:40px;height:40px;border-radius:50%;background:var(--white);display:block}
.nav{left:455px;top:82px;display:flex;gap:26px;font-size:15px;color:var(--white)}
.nav span{padding:5px 0}
.nav .active{background:var(--orange);padding:5px 14px;border-radius:3px}
.hero h1{left:100px;top:282px;font-size:60px;color:var(--white);letter-spacing:1px}
.hero p{left:100px;top:360px;width:520px;font-size:22px;line-height:34px;color:var(--white)}
.hero .btn{left:100px;top:458px;width:130px;height:40px;line-height:40px;font-size:16px}

/* for sale */
.sale-frame{left:100px;top:785px;width:380px;height:320px;border:2px solid var(--blue)}
.sale-img{left:110px;top:800px;width:370px;height:310px;background:linear-gradient(180deg,#cfd3d6,#7f868c);box-shadow:0 2px 8px rgba(0,0,0,.25)}
.sale h2{left:542px;top:812px;font-size:34px}
.sale p{left:542px;top:865px;width:580px;font-size:14px;line-height:27px;color:var(--muted)}
.sale .btn{left:542px;top:1080px;width:110px;height:34px;line-height:34px}

/* trailers */
.tr-band{left:0;top:1228px;width:1200px;height:360px;background:linear-gradient(180deg,var(--blue-deep),var(--blue))}
.tr-title{left:0;top:1295px;width:1200px;text-align:center;font-size:38px;color:var(--white)}
.card{width:295px;height:365px;background:var(--white);box-shadow:0 2px 8px rgba(0,0,0,.2);text-align:center}
.card .ph{height:190px}
.card h3{font-family:"Open Sans",sans-serif;font-weight:600;font-size:16px;margin-top:22px}
.card p{font-size:14px;line-height:22px;color:var(--muted);margin:10px 40px 0}
.card .btn{margin-top:14px;width:100px;height:26px;line-height:26px;font-size:12px}
.more{left:0;top:2180px;width:1200px;text-align:center;color:var(--blue);font-size:16px;font-weight:600}

/* services */
.services{left:0;top:2288px;width:1200px;height:627px;background:linear-gradient(180deg,#1b1b1b,#2c2c2c)}
.services h2{left:0;top:2370px;width:1200px;text-align:center;font-size:38px;color:var(--white)}
.svc{width:315px;height:260px;background:var(--white);top:2530px;text-align:center}
.svc h3{font-family:"Open Sans",sans-serif;font-size:19px;margin-top:100px}
.svc p{font-size:14px;line-height:24px;color:var(--muted);margin:12px 40px 0}
.svc-icon{width:124px;height:124px;border-radius:50%;top:2470px}
.svc-btn{top:2775px;width:110px;height:34px;line-height:32px;border-radius:17px;font-size:14px;text-align:center;background:var(--white);border:1px solid #ccc}

/* about */
.about h2{left:0;top:3010px;width:1200px;text-align:center;font-size:38px}
.about p{left:140px;top:3080px;width:920px;text-align:center;font-size:14px;line-height:27px;color:var(--muted)}
.video{left:130px;top:3237px;width:955px;height:458px;background:radial-gradient(circle at 50% 50%,#2b3f6a 0%,#0f1b33 70%,#0a0f1c 100%);border:6px solid #e5e5e5}
.play{left:578px;top:3436px}

/* testimonials */
.testi{left:0;top:3824px;width:1200px;height:488px;background:var(--grey-bg)}
.testi h2{left:0;top:3900px;width:1200px;text-align:center;font-size:38px}
.testi .q{left:578px;top:3978px;font-family:Georgia,serif;font-size:64px;line-height:60px;color:var(--orange)}
.testi p{left:170px;top:4050px;width:860px;text-align:center;font-size:14px;line-height:30px;color:var(--muted)}
.testi .who{left:0;top:4180px;width:1200px;text-align:center;font-size:17px;font-style:italic;color:var(--ink)}

/* map */
.map{left:0;top:4312px;width:1200px;height:350px;background:linear-gradient(135deg,#e4e4e4,#d2d2d2 50%,#e9e9e9)}
.pin{left:558px;top:4420px}

/* footer */
.footer{left:0;top:4662px;width:1200px;height:423px;background:var(--dark);color:#ccc}
.nl h3{left:285px;top:4705px;font-size:26px;color:var(--white);font-family:"Open Sans",sans-serif;font-weight:600;letter-spacing:1px}
.nl-input{left:470px;top:4705px;width:340px;height:36px;background:var(--white);border-radius:18px 0 0 18px;font-size:12px;color:#999;padding:11px 16px}
.nl-btn{left:800px;top:4705px;width:110px;height:36px;line-height:36px;background:var(--orange);border-radius:18px;color:var(--white);font-size:12px;text-align:center}
.fcol{top:4830px;font-size:11px;line-height:19px}
.fcol h4{font-size:13px;font-weight:600;color:var(--white);margin-bottom:6px;letter-spacing:.5px}
.fcol li{list-style:none}
.fcol li::before{content:"› ";color:var(--orange)}
.social{left:935px;top:4855px;display:flex;gap:10px}
.social .sq{width:24px;height:24px}
.copy{left:0;top:5028px;width:1200px;text-align:center;font-size:11px;color:#ccc}
</style>
</head>
<body>

<section class="hero abs" role="img" aria-label="Photograph of a caravan and trailers parked outdoors"></section>
<div class="topbar abs">
  <div class="contact abs"><span>&#9742; 03 9000 4812</span><span>&#9993; sales@dunlacktrailers.com.au</span></div>
  <div class="right abs">
    <svg width="14" height="14" viewBox="0 0 14 14"><circle cx="6" cy="6" r="4.5" fill="none" stroke="#fff" stroke-width="2"/><line x1="9.5" y1="9.5" x2="13" y2="13" stroke="#fff" stroke-width="2"/></svg>
    <span style="margin:0 22px">Login</span>
    <span class="sq"></span><span class="sq"></span><span class="sq"></span><span class="sq"></span>
  </div>
</div>
<div class="brand abs"><i></i>Dunlack Trailers</div>
<nav class="nav abs"><span class="active">Home</span><span>About Us</span><span>Trailers</span><span>Trailers Parts</span><span>Agents</span><span>Request A Quote</span><span>Contact Us</span></nav>
<div class="hero">
  <h1 class="abs" style="left:100px;top:282px">TRAILERS PARTS</h1>
</div>
<p class="abs" style="left:100px;top:360px;width:520px;font-size:22px;line-height:34px;color:#fff">Neque porro quisquam est qui dolorem ipsum quia dolor sit amet, consectetur dolorem</p>
<span class="btn btn-orange abs" style="left:100px;top:458px;width:130px;height:40px;line-height:40px;font-size:16px">View More</span>

<section class="sale">
  <div class="sale-frame abs"></div>
  <div class="sale-img abs" role="img" aria-label="Photograph of a galvanised trailer with an A-frame"></div>
  <h2 class="abs">Trailers For Sale</h2>
  <p class="abs">Dunlack Trailers is one of Melbourne's leading manufacturers and suppliers of high quality trailers. With our years of expertise in the trailer industry, we provide our trailers for sale with assurance of durability and reliability. Here, at Dunlack Trailers Melbourne, we offer the best range of trailers for sale. We offer a huge variety of new and used trailers to choose from. Dunlack are the experts in trailer sales. You are able to find all types of trailers including motorbike trailers, car trailers, box trailers, galvanized trailers, lawn mowing trailers.</p>
  <span class="btn btn-orange abs">Read More</span>
</section>

<section>
  <div class="tr-band abs"></div>
  <h2 class="tr-title abs">TRAILERS</h2>
  <div class="card abs" style="left:130px;top:1395px"><div class="ph" role="img" aria-label="Photograph of a box trailer" style="background:linear-gradient(180deg,#d9dde0,#8a9096)"></div><h3>Box Trailers</h3><p>Dolorem ipsum quia dolor quisquam est dolorem</p><span class="btn btn-blue">View Details</span></div>
  <div class="card abs" style="left:455px;top:1395px"><div class="ph" role="img" aria-label="Photograph of a cage trailer" style="background:linear-gradient(180deg,#6f8aa6,#2c3f52)"></div><h3>Cage Trailer</h3><p>Dolorem ipsum quia dolor quisquam est dolorem</p><span class="btn btn-blue">View Details</span></div>
  <div class="card abs" style="left:788px;top:1395px"><div class="ph" role="img" aria-label="Photograph of a car carrier trailer" style="background:linear-gradient(180deg,#c9a23a,#4a3d22)"></div><h3>Car Carrier Trailers</h3><p>Dolorem ipsum quia dolor quisquam est dolorem</p><span class="btn btn-blue">View Details</span></div>
  <div class="card abs" style="left:130px;top:1780px"><div class="ph" role="img" aria-label="Photograph of a red custom made trailer" style="background:linear-gradient(180deg,#d44a4a,#7a1f1f)"></div><h3>Custom Made Trailers</h3><p>Dolorem ipsum quia dolor quisquam est dolorem</p><span class="btn btn-blue">View Details</span></div>
  <div class="card abs" style="left:455px;top:1780px"><div class="ph" role="img" aria-label="Photograph of an enclosed trailer" style="background:linear-gradient(180deg,#d6d8da,#8d9194)"></div><h3>Enclosed Trailers</h3><p>Dolorem ipsum quia dolor quisquam est dolorem</p><span class="btn btn-blue">View Details</span></div>
  <div class="card abs" style="left:788px;top:1780px"><div class="ph" role="img" aria-label="Photograph of a flat bench trailer" style="background:linear-gradient(180deg,#9a9ea2,#2f3236)"></div><h3>Flat Bench Trailers</h3><p>Dolorem ipsum quia dolor quisquam est dolorem</p><span class="btn btn-blue">View Details</span></div>
  <div class="more abs">View More »</div>
</section>

<section>
  <div class="services abs" role="img" aria-label="Dark photograph of a workshop behind the services"></div>
  <h2 class="abs" style="left:0;top:2370px;width:1200px;text-align:center;font-size:38px;color:#fff">OUR SERVICES</h2>
  <div class="svc abs" style="left:95px"><h3>Trailers Parts</h3><p>It is a long established fact that a reader will be distracted by the readable content of a page</p></div>
  <div class="svc abs" style="left:442px"><h3>Repairs and Maintenance</h3><p>It is a long established fact that a reader will be distracted by the readable content of a page</p></div>
  <div class="svc abs" style="left:790px"><h3>Custom-Made Trailers</h3><p>It is a long established fact that a reader will be distracted by the readable content of a page</p></div>
  <svg class="svc-icon abs" style="left:190px" viewBox="0 0 124 124"><circle cx="62" cy="62" r="60" fill="#f39a1e" stroke="#fff" stroke-width="4"/><circle cx="62" cy="62" r="20" fill="none" stroke="#fff" stroke-width="6"/><circle cx="62" cy="62" r="6" fill="#fff"/><g stroke="#fff" stroke-width="8"><line x1="62" y1="30" x2="62" y2="40"/><line x1="62" y1="84" x2="62" y2="94"/><line x1="30" y1="62" x2="40" y2="62"/><line x1="84" y1="62" x2="94" y2="62"/></g></svg>
  <svg class="svc-icon abs" style="left:538px" viewBox="0 0 124 124"><circle cx="62" cy="62" r="60" fill="#2f5bb3" stroke="#fff" stroke-width="4"/><g stroke="#fff" stroke-width="6" stroke-linecap="round"><line x1="44" y1="44" x2="80" y2="80"/><line x1="80" y1="44" x2="44" y2="80"/></g><circle cx="42" cy="42" r="7" fill="none" stroke="#fff" stroke-width="4"/><circle cx="82" cy="42" r="7" fill="none" stroke="#fff" stroke-width="4"/></svg>
  <svg class="svc-icon abs" style="left:886px" viewBox="0 0 124 124"><circle cx="62" cy="62" r="60" fill="#f39a1e" stroke="#fff" stroke-width="4"/><rect x="34" y="46" width="40" height="26" fill="none" stroke="#fff" stroke-width="5"/><path d="M74 54h12l8 10v8H74z" fill="none" stroke="#fff" stroke-width="5"/><circle cx="46" cy="78" r="6" fill="#fff"/><circle cx="84" cy="78" r="6" fill="#fff"/></svg>
  <span class="svc-btn abs" style="left:198px">Read more</span>
  <span class="svc-btn abs" style="left:545px;background:#2f5bb3;color:#fff;border-color:#2f5bb3">Read more</span>
  <span class="svc-btn abs" style="left:893px">Read more</span>
</section>

<section class="about">
  <h2 class="abs">ABOUT US</h2>
  <p class="abs">At Dunlack Trailers, we are committed to being the most trusted Trailer Manufacturer of Australia by providing reliable and best quality Trailers to our customers. Established in 1962, Dunlack has been a leading manufacturer of comprehensive range of Garden &amp; construction tools. While we are Australia's fastest growing Trailer Company, Dunlack remains a family-owned business. Our vast experience in manufacturing has led to the production of exceptionally versatile trailers that include unique features.</p>
  <div class="video abs" role="img" aria-label="Company video with the brand mark on a dark blue background"></div>
  <svg class="play abs" width="56" height="56" viewBox="0 0 56 56"><circle cx="28" cy="28" r="27" fill="rgba(0,0,0,.55)" stroke="#fff" stroke-width="2"/><path d="M22 17l17 11-17 11z" fill="#fff"/></svg>
</section>

<section>
  <div class="testi abs"></div>
  <div class="testi">
    <h2 class="abs">TESTIMONIALS</h2>
    <div class="q abs">&ldquo;</div>
    <p class="abs">It is a long established fact that a reader will be distracted by the readable content of a page when looking at its layout. The point of using Lorem Ipsum is that it has a more-or-less normal distribution of letters, as opposed to using 'Content here, content here', making it look like readable English. Many desktop publishing packages and web page editors now use Lorem Ipsum as their default model text, and a search for 'lorem ipsum' will uncover many web sites still in their infancy.</p>
    <div class="who abs">-Neque porro quisquam</div>
  </div>
</section>

<div class="map abs" role="img" aria-label="Street map showing the business location"></div>
<svg class="pin abs" width="44" height="60" viewBox="0 0 44 60"><path d="M22 2C11 2 3 10 3 21c0 15 19 37 19 37s19-22 19-37C41 10 33 2 22 2z" fill="#e0453a"/><circle cx="22" cy="21" r="7" fill="#fff"/></svg>

<footer class="footer abs"></footer>
<div class="nl">
  <h3 class="abs">NEWSLETTER</h3>
  <div class="nl-input abs">email@example.com</div>
  <div class="nl-btn abs">SUBSCRIBE</div>
</div>
<div class="fcol abs" style="left:95px;color:#ccc"><h4>INFORMATION</h4><ul><li>Privacy Policy</li><li>Your Account</li><li>Advanced Search</li><li>Contact Us</li></ul></div>
<div class="fcol abs" style="left:352px;color:#ccc"><h4>CUSTOMER SERVICE</h4><ul><li>Trailers</li><li>Trailers Parts</li><li>Request A Quote</li><li>Return Policy</li></ul></div>
<div class="fcol abs" style="left:630px;color:#ccc;width:260px"><h4>CONTACT US</h4>Address : 42 Harbourview Road,<br>Eastfield, Victoria 3999<br>Phone : (03) 9000 4813 , (04) 9000 4814<br>Email : sales@dunlacktrailers.com.au</div>
<div class="fcol abs" style="left:935px;color:#ccc"><h4>FOLLOW US OUT THERE</h4></div>
<div class="social abs"><span class="sq"></span><span class="sq"></span><span class="sq"></span><span class="sq"></span></div>
<div class="copy abs">Copyright © 2018, All Rights Reserved</div>

</body>
</html>
```